Locksmith Business Cards

My father-in-law is in need of new business cards for his locksmith business and I need to impress him. Kindly help me out!

You can see the previous business card attached. It is a family run business in Glanmor Vale.

No individual names on the cards.

Key Things to Feature:
- The words "Prompt", "Local", "Reliable" (as you can see under the logo on the website)
- 24h Emergency Service
- Covering All of Glanmor Vale, the Fennick and Dunmere
- The color blue
- A key or a lock would be interesting (similar to the ones that come up when you google locksmith business card)

Optional (only if design includes bullet points, like the example below):
https://imgvaultexample.net/gallery/582214/77109/77109_9034417_582214_image.jpg
- Residential / Commercial / Automotive
- Alarms & Cameras
- Key Cutting & Safes

https://www.corswenydd-locksmiths.co.uk/

Industry/Entity Type

Locksmith

Contact Information for Business Card

01632 960 418
07700 900 562
corswenyddlocksmiths@mailbrook.example
Corswenydd Locksmiths, The Tan Barn, 7 Ferris Row, Porthgarreg LL99 4QX
www.corswenydd-locksmiths.co.uk

Requirements
Must have
• - The words "Prompt", "Local", "Reliable" (as you can see under the logo on the website)
• - 24h Emergency Service
• - Covering All of Glanmor Vale, the Fennick and Dunmere
Nice to have
• - A key or a lock would be interesting (similar to the ones that come up when you google locksmith business card)

```html
<!DOCTYPE html>
<html lang="en">
<head>
<meta charset="utf-8">
<title>Corswenydd Locksmiths – Business Card</title>
<link rel="stylesheet" href="https://fonts.googleapis.com/css2?family=Open+Sans:wght@400;600;700&family=Oswald:wght@400;500&display=swap">
<style>
  :root {
    --backdrop: #e9e6e1;
    --card-white: #ffffff;
    --navy: #232d6e;
    --rule-blue: #5563b0;
    --ink: #333338;
    --rule-grey: #d6d6d6;
    --back-dark: #25306f;
    --back-mid: #34449a;
    --back-light: #5468b6;
    --tagline: #e4e8f6;
    --white: #ffffff;
  }
  * { margin: 0; padding: 0; box-sizing: border-box; }
  html, body { width: 1200px; height: 900px; overflow: hidden; }
  body {
    position: relative;
    background: var(--backdrop);
    font-family: "Open Sans", Arial, sans-serif;
  }

  .card {
    position: absolute;
    box-shadow: 2px 3px 6px rgba(0,0,0,0.35);
  }

  /* ---------- Front ---------- */
  .card-front {
    left: 330px; top: 90px; width: 555px; height: 343px;
    background: var(--card-white);
  }
  .front-wordmark {
    position: absolute;
    left: 388px; top: 140px;
    width: 80px; height: 180px;
    writing-mode: vertical-rl;
    transform: rotate(180deg);
    font-family: "Oswald", "Arial Narrow", sans-serif;
    font-weight: 500;
    font-size: 32px;
    line-height: 38px;
    color: var(--navy);
    text-align: justify;
    text-align-last: justify;
  }
  .front-mark {
    position: absolute;
    left: 390px; top: 330px;
    width: 72px; height: 52px;
    background: var(--navy);
    border-radius: 4px;
  }
  .front-divider {
    position: absolute;
    left: 497px; top: 137px;
    width: 2px; height: 250px;
    background: var(--rule-blue);
  }
  .front-info {
    position: absolute;
    left: 525px; top: 141px;
    width: 252px;
    font-size: 14.5px;
    line-height: 20.3px;
    color: var(--ink);
  }
  .info-rule {
    height: 1px;
    background: var(--rule-grey);
    margin: 10px 0 6px;
  }
  .contact-line { display: flex; align-items: center; white-space: nowrap; }
  .contact-line svg { width: 12px; height: 12px; margin-right: 6px; fill: var(--navy); flex: none; }
  .emergency {
    margin-top: 13px;
    font-size: 15px;
    font-weight: 600;
    color: var(--navy);
  }

  /* ---------- Back ---------- */
  .card-back {
    left: 330px; top: 470px; width: 559px; height: 342px;
    background:
      radial-gradient(ellipse 320px 220px at 45% 20%, var(--back-light), transparent 75%),
      radial-gradient(ellipse 300px 200px at 85% 60%, rgba(84,104,182,0.55), transparent 75%),
      linear-gradient(160deg, var(--back-mid), var(--back-dark));
  }
  .back-mark {
    position: absolute;
    left: 458px; top: 536px;
    width: 68px; height: 68px;
    background: var(--white);
    border-radius: 6px;
  }
  .back-wordmark {
    position: absolute;
    left: 539px; top: 528px;
    font-family: "Oswald", "Arial Narrow", sans-serif;
    font-weight: 400;
    font-size: 44px;
    line-height: 51px;
    color: var(--white);
  }
  .tagline {
    position: absolute;
    left: 538px; top: 636px;
    font-weight: 600;
    font-size: 14.5px;
    letter-spacing: 0.3px;
    color: var(--tagline);
  }
  .services {
    position: absolute;
    left: 352px; top: 686px;
    list-style: none;
    font-family: "Oswald", "Arial Narrow", sans-serif;
    font-size: 19px;
    line-height: 31.5px;
    color: var(--white);
  }
  .services li::before {
    content: "";
    display: inline-block;
    width: 8px; height: 8px;
    border-radius: 50%;
    background: var(--white);
    margin: 0 5px 3px 0;
    vertical-align: middle;
  }
  .back-url {
    position: absolute;
    right: 338px; top: 757px;
    font-size: 15px;
    color: var(--white);
  }
</style>
</head>
<body>

  <section class="card card-front" aria-label="Business card front"></section>
  <div class="front-wordmark">CORSWENYDD LOCKSMITHS</div>
  <div class="front-mark"></div>
  <div class="front-divider"></div>
  <div class="front-info">
    <p>Corswenydd Locksmiths,<br>The Tan Barn, 7,<br>Ferris Row, Porthgarreg LL99 4QX</p>
    <div class="info-rule"></div>
    <p class="contact-line">
      <svg viewBox="0 0 24 24"><path d="M3 9c0-3 4-5 9-5s9 2 9 5v2h-5V9c0-1-2-1.5-4-1.5S8 8 8 9v2H3z"/><path d="M6 13h12l2 7H4z"/></svg>01632 960 418</p>
    <p class="contact-line">
      <svg viewBox="0 0 24 24"><path d="M7 1h10a2 2 0 0 1 2 2v18a2 2 0 0 1-2 2H7a2 2 0 0 1-2-2V3a2 2 0 0 1 2-2zm0 3v14h10V4z"/></svg>07700 900 562</p>
    <p class="contact-line">
      <svg viewBox="0 0 24 24"><path d="M2 5h20v14H2z"/><path d="M2 5l10 8 10-8" stroke="#fff" stroke-width="2" fill="none"/></svg>corswenyddlocksmiths@mailbrook.example</p>
    <p class="contact-line">
      <svg viewBox="0 0 24 24"><circle cx="12" cy="12" r="11"/><path d="M7 8c3 0 3 3 5 3s1 4 3 5M14 4c0 2 3 3 5 3" stroke="#fff" stroke-width="2" fill="none"/></svg>www.corswenydd-locksmiths.co.uk</p>
    <div class="info-rule"></div>
    <p class="emergency">24H EMERGENCY SERVICE</p>
    <p>Covering All of Glanmor Vale,<br>the Fennick and Dunmere</p>
  </div>

  <section class="card card-back" aria-label="Business card back"></section>
  <div class="back-mark"></div>
  <div class="back-wordmark">CORSWENYDD<br>LOCKSMITHS</div>
  <p class="tagline">PROMPT. LOCAL. RELIABLE</p>
  <ul class="services">
    <li>Residential / Commercial / Automotive</li>
    <li>Alarms &amp; Cameras</li>
    <li>Key Cutting &amp; Safes</li>
  </ul>
  <p class="back-url">www.corswenydd-locksmiths.co.uk</p>

</body>
</html>
```